Cardinal Lino Barreda Conferencia

We need a postcard 5 x 7 inches to promote a visit in our Catholic parish, from Cardinal Lino Barreda of El Salvador. We want a Catholic content/background, and a nice picture of the Cardinal, which you can find in searchly. Cardinal will be giving Mass and will be giving a conference talk after the Mass. He will give Mass at 7pm at Saint Brendan of Meadowfield Catholic Church, 51270 Quill Orchard Pkwy, Sterling, VA 20164, and then he will be giving a talk afterwards at Vellmore Hall, which is a hall in the parish. Please put the following in Spanish. "Misa 7pm," "Conferencia 7:45pm (en Vellmore Hall)" The conference title should be "Familia, Iglesia doméstica y transmisora de la fe" And also add that there will be refreshments after the talk at "Café y Pan Dulce 9pm" The date is "Jueves, Agosto 17, 2023"

```html
<!DOCTYPE html>
<html lang="es">
<head>
<meta charset="utf-8">
<title>Familia, Iglesia Doméstica y Transmisora de la Fe</title>
<link rel="stylesheet" href="https://fonts.googleapis.com/css2?family=Inter:ital,wght@0,400;0,700;0,800;1,400;1,700;1,800&family=Roboto+Condensed:wght@800;900&display=swap">
<style>
  :root {
    --purple-deep: #4a1f52;
    --purple-band: rgba(104, 48, 110, 0.92);
    --magenta: #b5364f;
    --rose: #d86a6a;
    --amber: #f4a24a;
    --glow: #fff1c8;
    --title-yellow: #f6f27a;
    --white: #ffffff;
    --coral: #fb5349;
    --vestment-red: #f0452f;
    --vestment-shadow: #c9301f;
    --cross-gold: #e8b86a;
  }
  * { margin: 0; padding: 0; box-sizing: border-box; }
  html, body { width: 1200px; height: 857px; overflow: hidden; }
  body { font-family: "Inter", sans-serif; }

  .postcard {
    position: relative;
    width: 1200px;
    height: 857px;
    overflow: hidden;
    background:
      radial-gradient(ellipse 380px 300px at 860px 90px, var(--glow) 0%, rgba(255, 214, 140, 0.85) 35%, rgba(244, 162, 74, 0) 100%),
      radial-gradient(ellipse 520px 420px at 600px 360px, rgba(232, 120, 110, 0.9) 0%, rgba(216, 106, 106, 0) 100%),
      linear-gradient(100deg, var(--purple-deep) 0%, #6b2c5c 25%, var(--magenta) 45%, var(--rose) 60%, var(--amber) 82%, #e45b3a 100%);
  }
  .postcard::after {
    content: "";
    position: absolute;
    inset: 0;
    background: linear-gradient(180deg, rgba(80, 30, 80, 0) 55%, rgba(90, 35, 95, 0.75) 100%);
    pointer-events: none;
  }

  .crucifix-art {
    position: absolute;
    left: 30px;
    top: 140px;
    width: 300px;
    height: 717px;
    background: radial-gradient(ellipse 150px 260px at 150px 300px, rgba(255, 226, 160, 0.75) 0%, rgba(232, 184, 106, 0.35) 50%, rgba(232, 184, 106, 0) 100%);
    z-index: 1;
  }

  .cardinal-photo {
    position: absolute;
    left: 790px;
    top: 190px;
    width: 410px;
    height: 667px;
    border-radius: 170px 170px 0 0;
    background: linear-gradient(180deg, rgba(200, 130, 110, 0.9) 0%, var(--vestment-red) 40%, var(--vestment-shadow) 100%);
    z-index: 2;
  }

  .event-date {
    position: absolute;
    left: 52px;
    top: 26px;
    font-weight: 700;
    font-size: 31px;
    color: var(--title-yellow);
    z-index: 3;
  }

  .event-title {
    position: absolute;
    left: 52px;
    top: 70px;
    font-family: "Roboto Condensed", sans-serif;
    font-weight: 800;
    font-size: 79px;
    line-height: 77px;
    color: var(--title-yellow);
    text-transform: uppercase;
    text-shadow: 0 2px 10px rgba(90, 30, 60, 0.35);
    z-index: 3;
  }

  .schedule {
    position: absolute;
    left: 330px;
    top: 268px;
    width: 510px;
    text-align: center;
    color: var(--white);
    z-index: 3;
  }
  .schedule-item {
    font-weight: 700;
    font-size: 41px;
    line-height: 58px;
  }
  .schedule-venue {
    font-weight: 400;
    font-size: 41px;
    line-height: 44px;
  }

  .refreshments {
    position: absolute;
    left: 307px;
    top: 526px;
    width: 505px;
    height: 118px;
    background: var(--coral);
    padding: 20px 0 0 26px;
    color: var(--white);
    z-index: 3;
  }
  .refreshments-lead {
    font-style: italic;
    font-weight: 400;
    font-size: 27px;
    line-height: 34px;
    letter-spacing: 0.5px;
  }
  .refreshments-main {
    font-style: italic;
    font-weight: 800;
    font-size: 40px;
    line-height: 46px;
  }

  .venue-band {
    position: absolute;
    left: 0;
    top: 723px;
    width: 613px;
    height: 100px;
    background: var(--purple-band);
    padding: 17px 0 0 36px;
    color: var(--white);
    z-index: 3;
  }
  .venue-name {
    font-weight: 700;
    font-size: 23px;
    line-height: 32px;
  }
  .venue-address {
    font-style: italic;
    font-weight: 400;
    font-size: 24px;
    line-height: 32px;
  }
</style>
</head>
<body>
  <main class="postcard">
    <div class="crucifix-art" role="img" aria-label="Crucifijo dorado iluminado por rayos de luz"></div>
    <div class="cardinal-photo" role="img" aria-label="Fotografía del Cardenal Lino Barreda con sotana roja y cruz pectoral"></div>

    <p class="event-date">Jueves, Agosto 17, 2023</p>
    <h1 class="event-title">Familia, Iglesia Doméstica<br>y Transmisora de la Fe</h1>

    <section class="schedule">
      <p class="schedule-item">Misa 7pm</p>
      <p class="schedule-item">Conferencia 7:45pm</p>
      <p class="schedule-venue">(en Vellmore Hall)</p>
    </section>

    <section class="refreshments">
      <p class="refreshments-lead">Refrescos después de la charla en</p>
      <p class="refreshments-main">Café y Pan Dulce 9pm</p>
    </section>

    <footer class="venue-band">
      <p class="venue-name">Saint Brendan of Meadowfield Catholic Church,</p>
      <p class="venue-address">51270 Quill Orchard Pkwy, Sterling, VA 20164</p>
    </footer>
  </main>
</body>
</html>
```